New flavour! New packaging for Velocity Energy Drink!

We need a new packaging designed to show off our new grape flavored energy drink! It will require box design with matching sachets!

Established in 2018 we are a fully Australian owned and operated business that started out with 2 gamers that got sick and tired of sugary energy drinks OR expensive powder from the USA.

We are an energy drink in the esports and gaming space. Our new product is an energy drink in powder in boxes of 30 sachets (please see attached for product example)

Please see example 1 and 2 for our competitors product. We would ideally like to go a bit more minimalist than them but still have a great color pop on black backing.

Target Market(s)

Gamer's and esports athletes between the ages or 18-30

Font styles to use
Sans Serif
Other font styles liked:
• Helvetica

Colors
886aae
ffffff

Requirements
Must have
• Black base/background.
• Vibrant purple N in the Velocity Logo.
• Same or slightly different shades of purple for some text and highlights.
• Black, white and some shades of a vibrant purple (for the grape flavor)
• ingredients list (may need to be reformatted to suit)
• Please see attached for legislative requirements on the box and sachets.
Nice to have
• minimalist design but enough to be eye catching and somewhat playful
• Twitter: @VLCT_FUEL
• Instagram: @VLCT_FUEL
• Facebook: @VLCTFUEL
Should not have
• OTHER COLORS.
• Overly complex designs.

```html
<!DOCTYPE html>
<html lang="en">
<head>
<meta charset="utf-8">
<title>Velocity Energy Drink – Grape Flavour Box</title>
<link rel="stylesheet" href="https://fonts.googleapis.com/css2?family=Russo+One&family=Michroma&display=swap">
<style>
  :root {
    --stage: #ececec;
    --black: #0b0a0d;
    --purple: #7440a8;
    --purple-top: #9a5ce0;
    --purple-side: #5a2f8c;
    --purple-bright: #8a55c8;
    --purple-text: #9a6ad6;
    --grape-dark: #3e1f6b;
    --grape-light: #8f74d8;
    --white: #ffffff;
    --silver: #c9c9cc;
  }
  * { box-sizing: border-box; margin: 0; padding: 0; }
  html, body {
    width: 1200px; height: 864px; overflow: hidden;
    background: var(--stage);
  }
  .panel { position: absolute; overflow: hidden; color: var(--white); font-family: "Michroma", sans-serif; }
  .panel-field { position: absolute; inset: 0; }

  /* Top panel */
  .box-top { left: 60px; top: 40px; width: 800px; height: 200px; background: var(--black); }
  .top-brand { position: absolute; left: 170px; top: 48px; }
  .top-brand .brand-name { font-size: 62px; }

  /* Side panel */
  .box-side {
    left: 860px; top: 240px; width: 220px; height: 420px;
    background: linear-gradient(180deg, var(--purple-side), #4a2576);
  }
  .side-name {
    position: absolute; left: 50%; top: 50%;
    transform: translate(-50%, -50%) rotate(-90deg);
    font-family: "Russo One", sans-serif; font-size: 52px; letter-spacing: 2px;
    color: var(--silver); white-space: nowrap;
  }

  /* Front panel */
  .box-front { left: 60px; top: 240px; width: 800px; height: 420px; background: var(--black); }
  .brand-name {
    font-family: "Russo One", sans-serif;
    font-size: 50px; letter-spacing: 1px; line-height: 1; color: var(--white);
  }
  .brand-sub {
    font-size: 9px; letter-spacing: 4px; text-align: right; margin-top: 6px; color: var(--white);
  }
  .front-brand { position: absolute; left: 28px; top: 52px; }
  .product-info { position: absolute; left: 42px; top: 214px; }
  .product-type { font-family: "Russo One", sans-serif; font-size: 18px; color: var(--purple-text); letter-spacing: 1px; }
  .product-desc { font-size: 8px; margin: 4px 0 6px 6px; letter-spacing: 0.4px; }
  .flavour-band {
    display: inline-block; background: var(--purple-bright);
    padding: 6px 22px 5px 18px;
    font-family: "Russo One", sans-serif; font-size: 24px; letter-spacing: 2px;
  }
  .product-extras { font-size: 8px; color: var(--purple-text); margin: 5px 0 0 24px; letter-spacing: 0.4px; }
  .serves {
    position: absolute; left: 46px; top: 340px;
    width: 40px; height: 38px; border: 1px solid var(--purple-text);
    text-align: center; padding-top: 4px;
  }
  .serves-count { font-family: "Russo One", sans-serif; font-size: 17px; line-height: 1; }
  .serves-label { font-size: 4.5px; letter-spacing: 0.4px; margin-top: 2px; }
  .tagline {
    position: absolute; left: 196px; top: 376px;
    font-size: 10px; letter-spacing: 1px; color: var(--purple-text); white-space: nowrap;
  }
  .tagline .tail { color: var(--silver); margin-left: 20px; }
  .grape-art {
    position: absolute; left: 470px; top: 90px; width: 200px; height: 220px;
    border-radius: 46% 42% 48% 40%;
    background: radial-gradient(circle at 40% 40%, var(--grape-light), var(--grape-dark) 80%);
  }
  .net-weight {
    position: absolute; right: 40px; bottom: 26px; text-align: center;
    font-family: "Russo One", sans-serif; color: var(--white);
  }
  .net-weight-main { font-size: 28px; line-height: 1; }
  .net-weight-detail { font-size: 15px; }
</style>
</head>
<body>
  <section class="panel box-top">
    <svg class="panel-field" width="800" height="200" viewBox="0 0 800 200" aria-hidden="true">
      <polygon points="800,30 800,200 360,200" fill="var(--purple-top)"/>
    </svg>
    <div class="top-brand">
      <div class="brand-name">VELOCITY</div>
      <div class="brand-sub">ENERGY DRINK</div>
    </div>
  </section>

  <main class="panel box-front">
    <svg class="panel-field" width="800" height="420" viewBox="0 0 800 420" aria-hidden="true">
      <polygon points="360,0 800,0 800,420 300,420 318,250 298,250 334,0" fill="var(--purple)"/>
    </svg>

    <div class="front-brand">
      <div class="brand-name">VELOCITY</div>
      <div class="brand-sub">ENERGY DRINK</div>
    </div>

    <div class="product-info">
      <div class="product-type">ENERGY DRINK</div>
      <div class="product-desc">FORMULATED CAFFEINATED BEVERAGE</div>
      <div class="flavour-band">GRAPE FLAVOUR</div>
      <div class="product-extras">WITH GINSENG &amp; CAFFEINE</div>
    </div>

    <div class="serves">
      <div class="serves-count">30</div>
      <div class="serves-label">SERVES</div>
    </div>

    <div class="tagline">FOR GAMERS,<span class="tail">BY GAMERS</span></div>

    <div class="grape-art" role="img" aria-label="Photograph of a bunch of purple grapes"></div>

    <div class="net-weight">
      <div class="net-weight-main">150 g</div>
      <div class="net-weight-detail">(30 x 5 g)</div>
    </div>
  </main>

  <section class="panel box-side">
    <div class="side-name">VELOCITY</div>
  </section>
</body>
</html>
```